Mobile Fitness snd Therapy Business Card Design

I need a business card designed for my mobile fitness and therapy business.

Please view the images that I have uploaded. I like the simplicity of the design that I have attached. I adapted it with my information

Target Market(s)

Those seeking personal training, injury rehabilitation or massage therapy.

Industry/Entity Type

Business

Contact Information for Business Card

Dylan Marwick - MSc, CAT(C), RMT, CSCS, Pn2
e-mail: dylan@vantrelo.com
website: www.vantrelo.com
instagram: @dylan_marwick

Font styles to use
Sans Serif

Colors
3176b5
0355a3

Requirements
Must have
• "Contact us to receive a FREE assessment"
• Services offered:
• Personal Training
• Golf Fitness
• Injury Rehab
• Massage Therapy
• Yoga
Nice to have
• Consistent colours with brand
• - Dark Blue: #232837
• - Blue: #5096f0
• Consistent look/feel with the website: www.vantrelo.com

```html
<!DOCTYPE html>
<html lang="en">
<head>
<meta charset="utf-8">
<title>Vantrelo Business Card</title>
<link href="https://fonts.googleapis.com/css2?family=Montserrat:wght@700&family=Roboto:wght@400;500&family=Roboto+Condensed:wght@700&display=swap" rel="stylesheet">
<style>
  :root {
    --backdrop: #e4e4e4;
    --navy: #232837;
    --paper: #f2f2f2;
    --blue: #2c5bd6;
    --blue-light: #5096f0;
    --white: #ffffff;
  }
  * { box-sizing: border-box; margin: 0; padding: 0; }
  html, body { width: 1200px; height: 960px; overflow: hidden; }
  body { background: var(--backdrop); position: relative; font-family: "Roboto", sans-serif; }

  .card { position: absolute; width: 600px; height: 344px; overflow: hidden; }
  .card--front { left: 314px; top: 113px; background: var(--paper); }
  .card--back { left: 311px; top: 472px; background: var(--navy); }

  .brand { position: absolute; left: 0; right: 0; text-align: center; }
  .brand__name {
    font-family: "Montserrat", sans-serif; font-weight: 700;
    font-size: 50px; letter-spacing: 5px; line-height: 1;
  }
  .brand__tagline {
    font-family: "Montserrat", sans-serif; font-weight: 700;
    font-size: 15px; letter-spacing: 2.4px; margin-top: 10px;
  }
  .card--front .brand { top: 72px; color: var(--navy); }
  .card--back .brand { top: 124px; color: var(--white); }

  .card__band { position: absolute; left: 0; right: 0; top: 200px; bottom: 0; background: var(--navy); }

  .person { position: absolute; left: 70px; top: 42px; color: var(--blue); font-family: "Roboto Condensed", sans-serif; font-weight: 700; }
  .person__name { font-size: 22px; line-height: 1; }
  .person__credentials { font-size: 10px; margin-top: 5px; }

  .contact { position: absolute; left: 362px; top: 40px; list-style: none; color: var(--white); font-size: 14px; }
  .contact__item { display: flex; align-items: center; height: 19px; }
  .contact__icon { width: 14px; height: 14px; margin-right: 8px; flex: none; }

  .offer {
    position: absolute; left: 58px; top: 259px; width: 483px; height: 33px;
    border-radius: 17px; background: var(--blue); color: var(--white);
    font-family: "Roboto Condensed", sans-serif; font-weight: 700; font-size: 20px;
    display: flex; align-items: center; justify-content: center;
  }
  .services { position: absolute; left: 0; right: 0; top: 298px; text-align: center; color: var(--white); font-size: 15px; }
  .services__sep { color: var(--blue-light); margin: 0 3px; }
</style>
</head>
<body>
  <section class="card card--front">
    <div class="brand">
      <div class="brand__name">VANTRELO</div>
      <div class="brand__tagline">NUTRITION - FITNESS - HEALTH</div>
    </div>
    <div class="card__band">
      <div class="person">
        <div class="person__name">DYLAN MARWICK</div>
        <div class="person__credentials">MSC, CAT(C), RMT, CSCS, PN2</div>
      </div>
      <ul class="contact">
        <li class="contact__item">
          <svg class="contact__icon" viewBox="0 0 14 14"><rect x="1" y="3" width="12" height="8" fill="#2c5bd6"/><path d="M1 3l6 5 6-5" fill="none" stroke="#232837" stroke-width="1.2"/></svg>
          dylan@vantrelo.com
        </li>
        <li class="contact__item">
          <svg class="contact__icon" viewBox="0 0 14 14"><circle cx="7" cy="7" r="6" fill="#2c5bd6"/><path d="M1 7h12M7 1c-3 3-3 9 0 12M7 1c3 3 3 9 0 12" fill="none" stroke="#232837" stroke-width="1"/></svg>
          www.vantrelo.com
        </li>
        <li class="contact__item">
          <svg class="contact__icon" viewBox="0 0 14 14"><circle cx="7" cy="7" r="6" fill="#2c5bd6"/></svg>
          @dylan_marwick
        </li>
      </ul>
    </div>
  </section>

  <section class="card card--back">
    <div class="brand">
      <div class="brand__name">VANTRELO</div>
      <div class="brand__tagline">NUTRITION - FITNESS - HEALTH</div>
    </div>
    <div class="offer">CONTACT US TO RECEIVE A FREE ASSESSMENT</div>
    <p class="services">Personal Training<span class="services__sep">|</span>Golf Fitness<span class="services__sep">|</span>Injury Rehab<span class="services__sep">|</span>Massage Therapy<span class="services__sep">|</span>Yoga</p>
  </section>
</body>
</html>
```